Medical Device - Case Study Template

We need a TEMPLATE that we can reuse to write various case studies about the medical equipment solutions we provide. It will be a double sided letter sized with a modern design that conveys a feeling of expertise, innovation and highly personable service AND be consistent with the brand guide. The content will be divided into a few sections:

- Situation (200-250 words)
- Challenge (100-120 words)
- Solution (100-120 words)
- Results (100-120 words)
- Conclusion (100-120 words)

Additionally, there will need to be a call to action, inviting people to send an email for more information and a short "About Talvo" section (approx. 40 words).

For device picture placeholders, feel free to use any random small benchtop medical device.

```html
<!DOCTYPE html>
<html lang="en">
<head>
<meta charset="utf-8">
<title>Talvo Case Study Template</title>
<link href="https://fonts.googleapis.com/css2?family=Barlow:wght@400;500&family=Barlow+Condensed:wght@600&family=Open+Sans:wght@400&display=swap" rel="stylesheet">
<style>
  :root {
    --bg: #7a9ebd;
    --orange: #f3862f;
    --steel: #6f92b3;
    --band: #7a9dbd;
    --body: #555b62;
    --paper-top: #eef2f6;
    --paper-bottom: #ffffff;
    --white: #ffffff;
  }
  * { margin: 0; padding: 0; box-sizing: border-box; }
  html, body { width: 1200px; height: 1200px; overflow: hidden; }
  body { background: var(--bg); font-family: "Barlow", sans-serif; position: relative; }

  .page {
    position: absolute; top: 287px; width: 484px; height: 627px;
    background: linear-gradient(160deg, var(--paper-top), var(--paper-bottom) 70%);
    overflow: hidden;
  }
  .page--cover { left: 92px; }
  .page--content { left: 624px; }

  /* cover */
  .cover-block {
    position: absolute; left: 268px; top: 0; width: 176px; height: 233px;
    background: var(--orange);
  }
  .cover-block__title {
    position: absolute; left: 27px; top: 52px;
    font-family: "Barlow Condensed", sans-serif; font-weight: 600;
    font-size: 62px; line-height: 60px; color: var(--white); letter-spacing: 0.5px;
  }
  .brand { position: absolute; left: 50px; top: 46px; }
  .brand__name {
    display: flex; align-items: center; gap: 8px;
    font-size: 30px; font-weight: 400; color: var(--steel); line-height: 1;
  }
  .brand__dot { width: 14px; height: 14px; border-radius: 50%; background: var(--orange); }
  .brand__tagline {
    margin-left: 22px; margin-top: 3px;
    font-size: 12.5px; font-weight: 500; color: var(--steel);
  }
  .device-title {
    position: absolute; left: 50px; top: 124px;
    font-size: 24.5px; font-weight: 500; line-height: 31px; color: var(--steel); letter-spacing: 0.3px;
  }
  .device-title__accent { color: var(--orange); }
  .device-title__rule {
    position: absolute; left: 50px; top: 230px; width: 183px; height: 3px; background: var(--orange);
  }
  .device-photo {
    position: absolute; left: 40px; top: 282px; width: 404px; height: 248px;
    background: linear-gradient(115deg, #eef3f8 0%, #dfe8f1 45%, #c8d8e8 70%, #9fb6cf 100%);
  }
  .cover-bar {
    position: absolute; left: 40px; top: 613px; width: 176px; height: 14px; background: var(--orange);
  }

  /* contact row */
  .contacts {
    position: absolute; display: flex; align-items: center;
    font-size: 11.3px; color: var(--steel); white-space: nowrap;
  }
  .contacts--cover { left: 40px; top: 563px; width: 404px; justify-content: space-between; }
  .contacts--content { left: 38px; top: 596px; width: 410px; justify-content: space-between; }
  .contacts__item { display: flex; align-items: center; gap: 4px; }
  .contacts__item svg { width: 7px; height: 7px; fill: var(--orange); }
  .contacts__accent { color: var(--orange); }
  .contacts__divider { width: 1px; height: 17px; background: var(--steel); opacity: 0.7; }

  /* content page */
  .top-bar {
    position: absolute; left: 273px; top: 0; width: 176px; height: 14px; background: var(--orange);
  }
  .section { position: absolute; left: 35px; width: 415px; }
  .section__heading {
    font-size: 19px; font-weight: 500; color: var(--orange); line-height: 22px; margin-bottom: 4px;
  }
  .section__text {
    font-family: "Open Sans", sans-serif; font-size: 6.2px; line-height: 8.7px;
    color: var(--body); text-align: justify; overflow: hidden;
  }
  .section--situation { top: 32px; }
  .section--situation .section__text { height: 79px; }
  .section--challenge { top: 153px; }
  .section--challenge .section__text { height: 44px; }
  .section--solution { top: 239px; }
  .section--solution .section__text { height: 44px; }
  .section--results { top: 325px; }
  .section--results .section__text { height: 44px; }
  .section--conclusion { top: 414px; }
  .section--conclusion .section__text { height: 53px; }

  .about {
    position: absolute; left: 0; top: 510px; width: 484px; height: 75px; background: var(--band);
  }
  .about__strip { position: absolute; left: 0; top: 0; width: 22px; height: 75px; background: var(--orange); }
  .about__heading {
    position: absolute; left: 35px; top: 9px;
    font-size: 19px; font-weight: 500; color: var(--white);
  }
  .about__text {
    position: absolute; left: 35px; top: 40px; width: 410px;
    font-family: "Open Sans", sans-serif; font-size: 7.3px; line-height: 10px; color: var(--white);
  }
</style>
</head>
<body>

<section class="page page--cover">
  <div class="brand">
    <div class="brand__name"><span class="brand__dot"></span>Talvo</div>
    <div class="brand__tagline">Medical Technology</div>
  </div>

  <div class="cover-block">
    <h1 class="cover-block__title">CASE<br>STUDY</h1>
  </div>

  <h2 class="device-title">YOUR<br>MEDICAL DEVICE<br><span class="device-title__accent">NAME HERE</span></h2>
  <div class="device-title__rule"></div>

  <div class="device-photo" role="img" aria-label="Photo of a benchtop laboratory microscope in a bright clinical lab"></div>

  <div class="contacts contacts--cover">
    <span class="contacts__item"><svg viewBox="0 0 10 10"><circle cx="5" cy="5" r="5"/></svg>www.<span class="contacts__accent">talvomedical</span>.com</span>
    <span class="contacts__divider"></span>
    <span class="contacts__item"><svg viewBox="0 0 10 8"><path d="M0 0h10v8H0z M0 0l5 4 5-4" /></svg>info@<span class="contacts__accent">talvomedical</span>.com</span>
    <span class="contacts__divider"></span>
    <span class="contacts__item"><svg viewBox="0 0 10 10"><path d="M2 0l2 2.5-1.2 1.5a6 6 0 0 0 3.2 3.2L7.5 6 10 8l-1.5 2C4 10 0 6 0 1.5z"/></svg>555 0142 387</span>
  </div>

  <div class="cover-bar"></div>
</section>

<section class="page page--content">
  <div class="top-bar"></div>

  <article class="section section--situation">
    <h3 class="section__heading">Situation</h3>
    <p class="section__text">A regional hospital network operating four outpatient clinics needed a dependable way to run routine blood and urine analysis on site. Samples were being couriered to a central laboratory twice a day, which meant that patients often waited more than forty-eight hours for results that guided their treatment. Clinicians reported that delays made follow-up visits harder to schedule and created extra calls for front desk staff. The network's leadership wanted faster answers without adding a full laboratory team at every location. Budgets were tight, floor space in each clinic was limited to a single bench, and any new equipment had to integrate with the existing electronic health record system. The procurement team also asked for predictable service costs, remote monitoring and on-site training for nurses who had little prior experience with analytical instruments. After reviewing several vendors, the network invited Talvo to assess its workflow, visit each clinic and propose a practical plan that fit the space, the staff and the schedule already in place.</p>
  </article>

  <article class="section section--challenge">
    <h3 class="section__heading">Challenge</h3>
    <p class="section__text">Each clinic had different opening hours, sample volumes and staff skills, so a single standard setup would not work everywhere. Two sites had unstable network connections, making data transfer to the record system unreliable. Nurses needed a device that could be learned in one afternoon, cleaned quickly between runs and serviced without closing the clinic. The network also required full traceability of every sample, clear quality control logs for audits and a rollout that would not interrupt patient care during the busy winter season.</p>
  </article>

  <article class="section section--solution">
    <h3 class="section__heading">Solution</h3>
    <p class="section__text">Talvo recommended a compact benchtop analyzer paired with a local data gateway that stores results when the connection drops and syncs them automatically once it returns. Our engineers configured each unit for the expected volume at its site and built simple on-screen guides for daily checks. Installation was completed after hours over two weeks. A Talvo specialist then spent a full day at every clinic training staff, followed by weekly remote reviews of quality control data during the first three months.</p>
  </article>

  <article class="section section--results">
    <h3 class="section__heading">Results</h3>
    <p class="section__text">Turnaround time for routine tests fell from two days to under forty minutes, allowing clinicians to discuss results with patients during the same visit. Courier costs dropped by more than sixty percent across the network. Quality control logs passed the first external audit without any findings. Staff confidence grew quickly, and nurses now run daily checks in less than ten minutes. Remote monitoring flagged two minor issues early, and both were resolved before they affected a single patient appointment.</p>
  </article>

  <article class="section section--conclusion">
    <h3 class="section__heading">Conclusion</h3>
    <p class="section__text">By placing the right device in the right place and supporting the people who use it, the hospital network turned a slow, costly process into a fast part of everyday care. The project showed that small clinics can offer laboratory quality results without a laboratory footprint. The network has since asked Talvo to extend the program to two new sites opening next year. For us, success means more than delivering equipment; it means staying close to every team, listening to their needs and improving the service long after installation. Email info@talvomedical.com to learn how we can help your clinics.</p>
  </article>

  <aside class="about">
    <div class="about__strip"></div>
    <h3 class="about__heading">About Talvo</h3>
    <p class="about__text">Talvo is a medical technology partner that supplies, installs and supports clinical equipment for hospitals and clinics. Our engineers and specialists help care teams work faster and with confidence.</p>
  </aside>

  <div class="contacts contacts--content">
    <span class="contacts__item"><svg viewBox="0 0 10 10"><circle cx="5" cy="5" r="5"/></svg>www.<span class="contacts__accent">talvomedical</span>.com</span>
    <span class="contacts__divider"></span>
    <span class="contacts__item"><svg viewBox="0 0 10 8"><path d="M0 0h10v8H0z M0 0l5 4 5-4" /></svg>info@<span class="contacts__accent">talvomedical</span>.com</span>
    <span class="contacts__divider"></span>
    <span class="contacts__item"><svg viewBox="0 0 10 10"><path d="M2 0l2 2.5-1.2 1.5a6 6 0 0 0 3.2 3.2L7.5 6 10 8l-1.5 2C4 10 0 6 0 1.5z"/></svg>555 0142 387</span>
  </div>
</section>

</body>
</html>
```